Business Card Design

New business, starting out small. High end residential/ commercial building company in Sydney Australia's prestigious Eastern suburbs, perfection is our motto and we want our marketing design to reflect that.

Therefore marketing towards high end clients. Looking for design concepts that will portray this image and will appeal to both male and females, prototype has been included- see images. Although we are open to ideas we have included this to give direction.

DARK Navy and white is the colour scheme, as per image provided. Logo ideas welcomed, however design is preferred simple, modern and sophisticated.

This business card will be the template and inspiration for website, t-shirt, banners etc to come so if you want the business, show us your design!

Industry/Entity Type

Marketing

Contact Information for Business Card

Company name: Tallow Ridge Building
Catch phrase: Your vision
Owner/operator: Garreth Pell
Phone: 0468172905
Website: www.tallowridgebuilding.com.au
Licence No 518294K
ABN 72 913 804
Email address
(displayed on back of card):info@tallowridgebuilding.com.au

```html
<!DOCTYPE html>
<html lang="en">
<head>
<meta charset="utf-8">
<title>Tallow Ridge Building – Business Card</title>
<link rel="stylesheet" href="https://fonts.googleapis.com/css2?family=Jost:wght@300;400;500&display=swap">
<style>
  :root {
    --navy: #0f1e33;
    --navy-light: #1b2d45;
    --white: #ffffff;
    --paper: #fbfbfa;
    --ink: #1a1a1a;
    --muted: #c9d1db;
    --backdrop: #e9e8e5;
  }
  * { box-sizing: border-box; margin: 0; padding: 0; }
  html, body {
    width: 1200px; height: 1000px; overflow: hidden;
    background: var(--backdrop);
    font-family: "Jost", sans-serif;
  }
  .canvas {
    width: 1200px; height: 1000px;
    display: flex; flex-direction: column; align-items: center; justify-content: center;
    gap: 40px;
  }
  .card {
    width: 740px; height: 430px; position: relative;
    box-shadow: 0 6px 20px rgba(0,0,0,0.18);
  }
  .card--front {
    background: var(--white);
    padding: 10px;
  }
  .card__face {
    width: 100%; height: 100%; position: relative;
    background: linear-gradient(160deg, var(--navy) 0%, var(--navy-light) 55%, var(--navy) 100%);
    color: var(--white);
  }
  .brand {
    position: absolute; top: 92px; right: 60px; width: 350px;
  }
  .brand__name {
    display: flex; align-items: center; gap: 14px;
    font-weight: 500; font-size: 25px; letter-spacing: 0.5px; text-transform: uppercase;
    padding-bottom: 8px;
    border-bottom: 1.5px solid var(--white);
  }
  .brand__mark {
    width: 20px; height: 20px; background: var(--white); flex: none;
  }
  .brand__tagline {
    text-align: center; margin-top: 8px;
    font-weight: 300; font-size: 19px; letter-spacing: 9px; text-transform: uppercase;
  }
  .person {
    position: absolute; top: 150px; left: 60px; text-align: right;
  }
  .person__name {
    font-weight: 300; font-size: 30px; letter-spacing: 1.5px; text-transform: uppercase;
  }
  .person__role {
    font-weight: 300; font-size: 15px; letter-spacing: 3px; text-transform: uppercase;
    color: var(--muted);
  }
  .contact {
    position: absolute; right: 50px; bottom: 42px;
    display: flex; flex-direction: column; align-items: flex-end; gap: 8px;
    font-weight: 300; font-size: 15px; letter-spacing: 1.5px;
  }
  .contact__row { display: flex; align-items: center; gap: 10px; }
  .contact__icon { width: 16px; height: 16px; }
  .card--back {
    background: var(--paper);
  }
  .email {
    position: absolute; right: 60px; bottom: 70px;
    font-weight: 400; font-size: 17px; letter-spacing: 3.5px; color: var(--ink);
  }
</style>
</head>
<body>
<main class="canvas">
  <section class="card card--front" aria-label="Business card front">
    <div class="card__face">
      <div class="brand">
        <div class="brand__name"><span class="brand__mark"></span>Tallow Ridge Building</div>
        <div class="brand__tagline">Your Vision</div>
      </div>
      <div class="person">
        <div class="person__name">Garreth Pell</div>
        <div class="person__role">Owner/Operator</div>
      </div>
      <div class="contact">
        <div class="contact__row">0468172905
          <svg class="contact__icon" viewBox="0 0 16 16" aria-hidden="true">
            <path d="M2 6 Q8 1 14 6 L12.5 8 L10.5 7 L10.5 5.5 Q8 4.8 5.5 5.5 L5.5 7 L3.5 8 Z" fill="#fff"/>
            <rect x="3.5" y="8.5" width="9" height="5.5" rx="1" fill="#fff"/>
            <circle cx="8" cy="11.2" r="1.5" fill="#0f1e33"/>
          </svg>
        </div>
        <div class="contact__row">www.tallowridgebuilding.com.au
          <svg class="contact__icon" viewBox="0 0 16 16" aria-hidden="true">
            <g fill="none" stroke="#fff" stroke-width="1.1">
              <circle cx="8" cy="8" r="6.5"/>
              <ellipse cx="8" cy="8" rx="3" ry="6.5"/>
              <line x1="1.5" y1="8" x2="14.5" y2="8"/>
              <line x1="2.5" y1="4.8" x2="13.5" y2="4.8"/>
              <line x1="2.5" y1="11.2" x2="13.5" y2="11.2"/>
            </g>
          </svg>
        </div>
        <div class="contact__row">Licence No 518294K ABN 72 913 804</div>
      </div>
    </div>
  </section>
  <section class="card card--back" aria-label="Business card back">
    <div class="email">info@tallowridgebuilding.com.au</div>
  </section>
</main>
</body>
</html>
```